Pelinta Party Planning Brochure

I am beginning a new Party Planning business and need a brochure outlining my services. We are offering a full range of party/event-related planning services. These include Catering Halls/Restaurants, Photography/Video, International DJ's and Bands, Flowers, Tuxedos/Gowns, Limousines and Specialized Entertainers such as Clowns and Face Painters, Middle Eastern Belly Dancers, and Musical Impersonators (specifically, Dale Morrow impersonator). I would like a festive design, showing people having a good time in a festive setting. No vulgar or inappropriate photos or language, please.

Target Market(s)

Primarily, newly engaged couples. As for ethnic preference, Greek-speaking clientele.

Future brides, new parents and newly engaged couples, primarily in the Greek market.

Industry/Entity Type

Business

Font styles to use
Sans Serif

Colors
33a6d7

Requirements
Must have
• Mention of speaking Greek and Spanish. Festive design. I need to have this phrase included exactly as you see it
• I need the brochure to look, read and exude "happy".
Nice to have
• Pictures of party atmosphere. A lively room.
Should not have
• No vulgarities, no inappropriate pictures. No drunken photos or offensive images.

```html
<!DOCTYPE html>
<html lang="en">
<head>
<meta charset="utf-8">
<title>Pelinta Party Planning Brochure</title>
<link rel="stylesheet" href="https://fonts.googleapis.com/css2?family=Arimo:ital,wght@0,400;0,700;1,400&display=swap">
<style>
  :root {
    --page: #ffffff;
    --sky: #8fd0ea;
    --sky-deep: #6fc1e3;
    --sky-pale: #e8f5fb;
    --ink: #111111;
    --navy-text: #2b5490;
    --navy-mark: #0a2a8a;
    --soft-grey: #3c4650;
    --white: #ffffff;
  }
  * { margin: 0; padding: 0; box-sizing: border-box; }
  html, body {
    width: 1200px; height: 1000px; overflow: hidden;
    background: var(--page);
    font-family: "Arimo", Arial, sans-serif;
  }
  .canvas { position: relative; width: 1200px; height: 1000px; }

  .spread { position: absolute; left: 329px; width: 542px; overflow: hidden; }
  .spread--outside {
    top: 60px; height: 383px;
    background:
      radial-gradient(circle at 14% 12%, rgba(255,255,255,.35) 0 6px, transparent 7px),
      radial-gradient(circle at 47% 9%, rgba(255,255,255,.35) 0 8px, transparent 9px),
      radial-gradient(circle at 58% 78%, rgba(255,255,255,.3) 0 7px, transparent 8px),
      radial-gradient(circle at 97% 52%, rgba(255,255,255,.3) 0 9px, transparent 10px),
      radial-gradient(circle at 75% 88%, rgba(255,255,255,.3) 0 6px, transparent 7px),
      radial-gradient(ellipse 55% 60% at 48% 48%, var(--sky-pale) 0%, rgba(232,245,251,.4) 55%, transparent 80%),
      linear-gradient(180deg, var(--sky) 0%, var(--sky-deep) 100%);
  }
  .spread--inside {
    top: 557px; height: 384px;
    background:
      radial-gradient(ellipse 62% 62% at 50% 50%, var(--white) 0%, var(--white) 78%, rgba(255,255,255,.6) 90%, transparent 100%),
      linear-gradient(180deg, var(--sky) 0%, var(--sky-deep) 100%);
  }

  .photo { position: absolute; }
  .photo--vintage-car { left: 33px; top: 15px; width: 128px; height: 233px;
    background: linear-gradient(160deg, #e8ecee 0%, #c9cfd3 50%, #5a5f52 100%); }
  .photo--table-setting { left: 376px; top: 15px; width: 129px; height: 233px;
    background: linear-gradient(180deg, #c7dbe6 0%, #b49ad8 45%, #3a39a8 70%, #eceff3 100%); }
  .photo--ballroom { left: 33px; top: 17px; width: 134px; height: 104px;
    background: linear-gradient(180deg, #b9b3a4 0%, #8d8576 45%, #e6e3dc 100%); }
  .photo--toast { left: 187px; top: 260px; width: 170px; height: 94px;
    background: linear-gradient(120deg, #d8cfc9 0%, #b6a7a6 50%, #e7e1dc 100%); }
  .photo--centerpiece { left: 377px; top: 173px; width: 137px; height: 181px;
    background: linear-gradient(180deg, #d9dde3 0%, #9b8cc4 35%, #e9ecef 65%, #f4f5f6 100%); }

  .rule { position: absolute; left: 38px; width: 128px; height: 1px; background: rgba(255,255,255,.55); }

  .contact { position: absolute; left: 20px; top: 265px; width: 220px; text-align: center;
    font-style: italic; font-size: 8px; line-height: 1; color: var(--soft-grey); }
  .contact p { margin-bottom: 9px; }
  .contact p.tight { margin-bottom: 4px; }

  .cover-title { position: absolute; left: 384px; top: 276px; width: 146px; text-align: center;
    font-size: 11px; color: var(--ink); }
  .cover-tagline { position: absolute; left: 384px; top: 305px; width: 146px; text-align: center;
    font-size: 12px; color: var(--white); }
  .web { position: absolute; left: 398px; top: 357px; width: 122px; text-align: center;
    font-size: 6px; font-weight: 700; color: var(--white); }
  .web strong { color: var(--navy-mark); }

  .col { position: absolute; text-align: center; color: var(--navy-text); }
  .col p { position: absolute; left: 0; width: 100%; white-space: nowrap; }
  .col--intro { left: 10px; width: 180px; font-size: 9px; }
  .col--services { left: 190px; width: 170px; font-size: 6px; }
  .col--events { left: 362px; width: 166px; font-size: 6px; }
</style>
</head>
<body>
<main class="canvas">

  <section class="spread spread--outside" aria-label="Brochure outside">
    <div class="photo photo--vintage-car" role="img" aria-label="Photo of a white vintage wedding car"></div>
    <div class="rule" style="top:258px"></div>
    <div class="contact">
      <p>Call Us Today at (555) 014-2273</p>
      <p class="tight">or Log On to</p>
      <p>www.pelintapartyplanning.com</p>
      <p class="tight">and Let Us Make Your Special Event</p>
      <p>One That Will Last a Lifetime!</p>
    </div>
    <div class="rule" style="top:365px"></div>

    <div class="photo photo--table-setting" role="img" aria-label="Photo of a table setting with champagne glasses and purple flowers"></div>
    <h1 class="cover-title" style="font-weight:400">Pelinta Party Planning</h1>
    <p class="cover-tagline">Is Your Only Choice</p>
    <p class="web">www.<strong>pelintapartyplanning</strong>.com</p>
  </section>

  <section class="spread spread--inside" aria-label="Brochure inside">
    <div class="photo photo--ballroom" role="img" aria-label="Photo of a decorated banquet hall with chandelier"></div>
    <div class="col col--intro">
      <p style="top:134px">Pelinta Party Planning</p>
      <p style="top:173px">Is Your Only Choice</p>
      <p style="top:212px">For Complete Plyrty</p>
      <p style="top:231px">Entertainment Services</p>
      <p style="top:309px">Hablamos Espanol</p>
      <p style="top:328px">Milame Ellinika</p>
    </div>

    <div class="col col--services">
      <p style="top:17px">We are Affiliated With the Best</p>
      <p style="top:62px">Catering Halls &amp; Restaurants</p>
      <p style="top:106px">Photo/Video, International DJs/Bands</p>
      <p style="top:151px">Limos, Wedding Gowns &amp; Bridesmaids Dresses</p>
      <p style="top:196px">Tuxedos, Flowers</p>
      <p style="top:225px">and Specialized Entertainers</p>
    </div>
    <div class="photo photo--toast" role="img" aria-label="Photo of guests raising glasses in a toast"></div>

    <div class="col col--events">
      <p style="top:17px">Weddings, Birthdays, Anniversaries, Sweet 16s</p>
      <p style="top:50px">Quinceneras, Corporate Events</p>
      <p style="top:74px">or Any Event of Any Kind</p>
      <p style="top:117px">We Are Ready To Help You</p>
      <p style="top:131px">Put Together An Unforgettable Experience</p>
      <p style="top:145px">For Everyone To Remember</p>
    </div>
    <div class="photo photo--centerpiece" role="img" aria-label="Photo of a tall floral centerpiece on a banquet table"></div>
  </section>

</main>
</body>
</html>
```